Website for Nonprofit for kids whose parents have been wounded

We need a web design for a nonprofit that serves children who have been severely burned as well as those whose parents have been wounded during military service. We will be based out of hospitals and will need a format that will encourage trust, safety, and respect. We are stick with a lot of red white and blue. We will also be looking to have a space for donations.

Target Market(s)

Kids and parents of military veterans

Industry/Entity Type

Non Profit

Number of Pages Required

5+ page

Font styles to use
Serif
Decorative

Colors
ec1f27
ffffff
0255a3

Requirements
Must have
• Be both appealing to children and adults. Create a reputable face for our organization. We need an area for donations.
Nice to have
• Something unique

```html
<!DOCTYPE html>
<html lang="en">
<head>
<meta charset="utf-8">
<title>Brightside Kids — Children's Support Nonprofit</title>
<link rel="stylesheet" href="https://fonts.googleapis.com/css2?family=Open+Sans:wght@400;600;700&family=Oswald:wght@300;400&display=swap">
<style>
:root{
  --red:#ec1f27;
  --blue:#0255a3;
  --sky:#2a9fe0;
  --white:#ffffff;
  --ink:#333;
  --muted:#777;
  --light:#f3f3f3;
  --navy:#1b2430;
  --navy-deep:#131a23;
  --line:#d9d9d9;
}
*{box-sizing:border-box;margin:0;padding:0}
html,body{width:692px;height:1200px;overflow:hidden}
body{font-family:"Open Sans",Arial,sans-serif;color:var(--ink);background:var(--white);font-size:7px;line-height:1.5}
.page{width:692px;height:1200px;position:relative}

/* header */
.site-header{height:68px;position:relative;background:var(--white)}
.brand{position:absolute;left:22px;top:14px;display:flex;align-items:center;gap:6px}
.brand-square{width:10px;height:10px;background:var(--red)}
.brand-name{font-family:"Open Sans",sans-serif;font-weight:700;font-size:13px;color:var(--ink)}
.contact-bar{position:absolute;right:22px;top:9px;display:flex;gap:14px;font-size:7px;color:var(--muted);align-items:center}
.contact-bar span{display:flex;align-items:center;gap:4px}
.main-nav{position:absolute;right:22px;top:30px;display:flex;align-items:center}
.main-nav a{font-size:7.5px;color:var(--ink);text-decoration:none;padding:0 14px;font-weight:600}
.main-nav a.active{color:var(--red)}
.search-btn{width:18px;height:18px;background:#222;display:flex;align-items:center;justify-content:center;margin-left:6px}

/* hero */
.hero{position:relative;height:292px;background:linear-gradient(90deg,var(--sky) 0 72px,transparent 72px 620px,var(--sky) 620px)}
.hero-photo{position:absolute;left:72px;top:0;width:548px;height:200px;background:linear-gradient(160deg,#8f7b63 0%,#b79c7e 35%,#6e5847 70%,#4d3c31 100%)}
.hero-caption{position:absolute;left:72px;width:548px;top:150px;text-align:center;color:var(--white)}
.hero-caption h1{font-family:"Oswald",sans-serif;font-weight:400;font-size:17px;letter-spacing:.5px}
.hero-caption p{font-size:6.5px;margin-top:2px}
.donate-bar{position:absolute;left:72px;top:200px;width:548px;height:34px;background:rgba(255,255,255,.92);display:flex;align-items:center;gap:9px;padding:0 12px;border-bottom:3px solid var(--blue)}
.donate-bar .field{flex:1;height:17px;border:1px solid var(--line);background:var(--white);font-size:6.5px;color:#999;padding:3px 5px}
.btn-red{background:var(--red);color:var(--white);font-weight:700;font-size:7px;border:none;display:inline-flex;align-items:center;gap:6px;padding:0 10px;height:19px;letter-spacing:.3px}

/* features */
.features{display:flex;gap:16px;padding:0 80px;margin-top:-44px;position:relative}
.feature{flex:1;display:flex;gap:7px;align-items:flex-start}
.feature-icon{width:32px;height:32px;border-radius:50%;border:2px solid var(--red);display:flex;align-items:center;justify-content:center;flex:none;background:var(--white)}
.feature h3{font-size:7.5px;color:var(--blue);font-weight:700;margin-bottom:2px}
.feature p{font-size:6px;color:var(--muted);line-height:1.45}

/* about */
.about{text-align:center;padding:44px 90px 0}
.section-title{font-family:"Oswald",sans-serif;font-weight:300;font-size:25px;color:#222;letter-spacing:.5px}
.rule{width:40px;height:1px;background:#999;margin:3px auto 10px}
.about p{font-size:6.5px;color:var(--muted);text-align:left;line-height:1.6}
.about .btn-red{margin-top:14px}

/* donate grid */
.causes{margin-top:32px;background:var(--light);padding:28px 0 0;text-align:center;height:454px}
.causes .subtitle{font-size:6.5px;color:#555;letter-spacing:.3px;margin-top:-4px}
.cause-grid{display:grid;grid-template-columns:repeat(3,168px);grid-auto-rows:148px;gap:10px;justify-content:center;margin-top:16px}
.cause{position:relative}
.cause.c1{background:linear-gradient(135deg,#4f9bd6,#2a74b8)}
.cause.c2{background:linear-gradient(135deg,#b7a08d,#7d6a5c)}
.cause.c3{background:linear-gradient(135deg,#d9c3ae,#9f7e66)}
.cause.c4{background:linear-gradient(135deg,#6a4a38,#3b2a20)}
.cause.c5{background:linear-gradient(135deg,#a89c88,#6f6555)}
.cause.c6{background:linear-gradient(135deg,#c9b7a2,#8a705a)}
.cause-zoom{position:absolute;left:50%;top:50%;width:18px;height:18px;margin:-9px 0 0 -9px;background:var(--white);display:flex;align-items:center;justify-content:center}

/* footer */
.site-footer{position:absolute;left:0;right:0;top:1010px;height:190px;background:var(--navy);color:#bbb}
.footer-cols{display:flex;padding:22px 50px 0;gap:24px}
.footer-col{flex:1}
.footer-col h4{font-size:7.5px;color:var(--white);font-weight:700;margin-bottom:9px}
.footer-col ul{list-style:none}
.footer-col li{font-size:6.5px;margin-bottom:5px;padding-left:8px;position:relative}
.footer-col li::before{content:"";position:absolute;left:0;top:3px;border-left:3px solid #bbb;border-top:2px solid transparent;border-bottom:2px solid transparent}
.newsletter p{font-size:6.5px;margin-bottom:6px}
.newsletter .input{height:15px;width:110px;background:var(--white);font-size:6px;color:#999;padding:2px 5px;margin-bottom:5px}
.newsletter .btn-red{height:16px;padding:0 14px}
.social{display:flex;gap:5px;margin-bottom:14px}
.social span{width:13px;height:13px;border-radius:50%;background:#8a93a0}
.footer-brand{display:flex;align-items:center;gap:5px}
.footer-brand .brand-name{font-size:11px;color:var(--white)}
.copyright{position:absolute;left:0;right:0;bottom:0;height:22px;background:var(--navy-deep);text-align:center;font-size:6px;line-height:22px;color:#8a8f96}
</style>
</head>
<body>
<div class="page">

  <header class="site-header">
    <div class="brand"><span class="brand-square"></span><span class="brand-name">Brightside Kids</span></div>
    <div class="contact-bar">
      <span><svg width="8" height="8" viewBox="0 0 10 10"><path d="M2 1l2 2-1 1.5c.7 1.3 1.6 2.2 2.9 2.9L7.4 6l2 2-1.4 1.6C4.5 9.3.7 5.5.4 2.4z" fill="#888"/></svg>555-018-2400</span>
      <span><svg width="9" height="7" viewBox="0 0 10 8"><rect x=".5" y=".5" width="9" height="7" fill="none" stroke="#888"/><path d="M.5.5L5 4.5 9.5.5" fill="none" stroke="#888"/></svg>hello@brightsidekids.org</span>
    </div>
    <nav class="main-nav">
      <a class="active" href="#">HOME</a>
      <a href="#">WHO WE ARE</a>
      <a href="#">WHAT WE DO</a>
      <a href="#">DONATE</a>
      <a href="#">CONTACT</a>
      <span class="search-btn"><svg width="8" height="8" viewBox="0 0 10 10"><circle cx="4" cy="4" r="3" fill="none" stroke="#fff" stroke-width="1.4"/><path d="M6.2 6.2L9 9" stroke="#fff" stroke-width="1.4"/></svg></span>
    </nav>
  </header>

  <section class="hero">
    <div class="hero-photo" role="img" aria-label="Photo of smiling children standing together"></div>
    <div class="hero-caption">
      <h1>LOREM IPSUM IS SIMPLY DUMMY</h1>
      <p>Caring for children and families through every step of recovery and healing.</p>
    </div>
    <form class="donate-bar">
      <div class="field">First Name...</div>
      <div class="field">Last Name...</div>
      <div class="field">Email Address...</div>
      <div class="field">Amount $...</div>
      <span class="btn-red">DONATE NOW <svg width="9" height="7" viewBox="0 0 10 8"><path d="M0 4h8M5 1l3 3-3 3" fill="none" stroke="#fff" stroke-width="1.4"/></svg></span>
    </form>
  </section>

  <section class="features">
    <div class="feature">
      <span class="feature-icon"><svg width="14" height="14" viewBox="0 0 14 14"><circle cx="7" cy="7" r="6" fill="none" stroke="#0255a3" stroke-width="1.5"/><circle cx="7" cy="7" r="2.5" fill="#ec1f27"/></svg></span>
      <div><h3>OUR MISSION</h3><p>Lorem ipsum is simply dummy text of the printing and typesetting industry since the standard.</p></div>
    </div>
    <div class="feature">
      <span class="feature-icon"><svg width="14" height="13" viewBox="0 0 14 13"><path d="M7 12S1 8 1 4.2C1 2.3 2.4 1 4 1c1.3 0 2.3.7 3 1.8C7.7 1.7 8.7 1 10 1c1.6 0 3 1.3 3 3.2C13 8 7 12 7 12z" fill="#ec1f27"/></svg></span>
      <div><h3>WE CARE</h3><p>Lorem ipsum is simply dummy text of the printing and typesetting industry since the standard.</p></div>
    </div>
    <div class="feature">
      <span class="feature-icon"><svg width="14" height="14" viewBox="0 0 14 14"><rect x="1" y="5" width="12" height="8" fill="none" stroke="#0255a3" stroke-width="1.5"/><path d="M7 1v8M4 4l3-3 3 3" fill="none" stroke="#ec1f27" stroke-width="1.5"/></svg></span>
      <div><h3>DONATE</h3><p>Lorem ipsum is simply dummy text of the printing and typesetting industry since the standard.</p></div>
    </div>
  </section>

  <section class="about">
    <h2 class="section-title">ABOUT US</h2>
    <div class="rule"></div>
    <p>Lorem Ipsum is simply dummy text of the printing and typesetting industry. Lorem Ipsum has been the industry's standard dummy text ever since the 1500s, when an unknown printer took a galley of type and scrambled it to make a type specimen book. It has survived not only five centuries, but also the leap into electronic typesetting, remaining essentially unchanged. Lorem Ipsum is simply dummy text of the printing and typesetting industry. Lorem Ipsum has been the industry's standard dummy text ever since.</p>
    <span class="btn-red">VIEW MORE</span>
  </section>

  <section class="causes">
    <h2 class="section-title">DONATE FOR THEM</h2>
    <div class="rule"></div>
    <p class="subtitle">OUR SERVICES FOR CHILDREN WHOSE PARENTS HAVE BEEN WOUNDED DURING MILITARY SERVICE</p>
    <div class="cause-grid">
      <div class="cause c1" role="img" aria-label="Photo of a child, shown with a blue highlight overlay"><span class="cause-zoom"><svg width="9" height="9" viewBox="0 0 10 10"><circle cx="4" cy="4" r="3" fill="none" stroke="#2a74b8" stroke-width="1.4"/><path d="M6.2 6.2L9 9" stroke="#2a74b8" stroke-width="1.4"/></svg></span></div>
      <div class="cause c2" role="img" aria-label="Photo of hands held together"></div>
      <div class="cause c3" role="img" aria-label="Photo of a young girl"></div>
      <div class="cause c4" role="img" aria-label="Close-up photo of a child"></div>
      <div class="cause c5" role="img" aria-label="Photo of a child sitting outdoors"></div>
      <div class="cause c6" role="img" aria-label="Photo of a smiling child"></div>
    </div>
  </section>

  <footer class="site-footer">
    <div class="footer-cols">
      <div class="footer-col">
        <h4>MAIN MENU</h4>
        <ul><li>Home</li><li>Who we are</li><li>What we do</li><li>Donate</li><li>Contact</li></ul>
      </div>
      <div class="footer-col">
        <h4>QUICK LINK</h4>
        <ul><li>Customer Policy</li><li>Our Policy</li><li>Terms and conditions of use</li><li>Secure payment</li><li>Sitemap</li></ul>
      </div>
      <div class="footer-col newsletter">
        <h4>NEWSLETTER</h4>
        <p>Lorem ipsum dolor sit amet</p>
        <div class="input">Your Name</div>
        <div class="input">Email ID</div>
        <span class="btn-red">SEND</span>
      </div>
      <div class="footer-col">
        <h4>GET IN TOUCH</h4>
        <div class="social"><span></span><span></span><span></span><span></span></div>
        <div class="footer-brand"><span class="brand-square"></span><span class="brand-name">Brightside Kids</span></div>
      </div>
    </div>
    <div class="copyright">Copyright © 2016 Brightside Kids. All rights reserved.</div>
  </footer>

</div>
</body>
</html>
```